依頼概要
■依頼の目的/概要
大型施設の共有スペースに展示する商品のPOPのデザインをお願いします。
展示の全体イメージがありますのでそれに合わせたイメージで制作して下さい。

■依頼詳細
大型SC内の新店舗の商品展示用のPOPになります。
展示イメージに合うようにPOPの制作をして下さい。
前回の展示のPOPを参考にアップしておきますが、同じような配置にする必要はございません。
前回は背景色などは変えずに、商品名、金額等を、レディース、メンズ、キッズの三種類に色分けして区別しておりました。
今回はキッズはないのですが、レディース、メンズ、雑貨と別れておりますので、うまく区別できるような工夫をお願いします。
サイズは A4縦サイズ。
店舗によって商品、金額、アイテム数は変化するので、変更できるような仕様にして下さい。
フォントはモリサワでしたら入っております。
採用後は使用フォントを納品データと共にお知らせください。

■重視する点
Illustrator・Photoshopの経験必須でお願いします。
新店舗のPOPになりますので、」お客様の目に留まるようなデザインが望ましいです。

■継続依頼について
弊社ではこういった案件が多くあり、次回は母の日、父の日等もありますので、継続的依頼できるありがたいです。

その他何かご不明な点がございましたら、お気軽にご質問下さい。
よろしくお願いいたします。
参考用イメージをアップします。

今回の展示イメージ
前回のPOPイメージ

の2点です。
1店舗の最大アイテム数は6になります。
前回のPOP参考例はあくまで参考です。
同じように作作らなくても良いので参考程度にして頂ければ幸いです。
展示イメージにある通り、POPは各マネキン、雑貨の前に置くものになります。
新店舗のオープンなのでワクワクするようなイメージで制作してもらえればと思います。
集まりが少ないので当選額を上乗せします。
それに伴い期間も延長いたします。
ご応募いただきありがとうございました。

見やすくイメージに沿っていたため。

たくさんのご参加ありがとうございました。
ぜひ次回もご参加下さい。

```html
<!DOCTYPE html>
<html lang="ja">
<head>
<meta charset="utf-8">
<title>NEW＆RENEWAL POP</title>
<link rel="stylesheet" href="https://fonts.googleapis.com/css2?family=Shippori+Mincho:wght@400;500&family=EB+Garamond:wght@400;500&display=swap">
<style>
  :root {
    --bg-light: #f3f5ea;
    --bg-mid: #e3ead2;
    --bg-deep: #d2dcbc;
    --card: #fbfbf8;
    --card-edge: #e6e6df;
    --ink: #4a4a45;
    --ink-soft: #6f6f68;
    --rule: #8d8d84;
    --footer: #ffffff;
    --figure: #dcdcd4;
    --figure-light: #ececE6;
    --slot-line: #9a9a92;
  }
  html, body {
    margin: 0;
    padding: 0;
    overflow: hidden;
  }
  body {
    width: 846px;
    height: 1200px;
    position: relative;
    font-family: "Shippori Mincho", serif;
    color: var(--ink);
    background:
      radial-gradient(ellipse at 20% 30%, var(--bg-light) 0%, transparent 55%),
      radial-gradient(ellipse at 80% 70%, var(--bg-light) 0%, transparent 50%),
      radial-gradient(ellipse at 85% 15%, var(--bg-deep) 0%, transparent 45%),
      radial-gradient(ellipse at 10% 85%, var(--bg-deep) 0%, transparent 45%),
      var(--bg-mid);
  }
  .header {
    position: absolute;
    top: 0;
    left: 0;
    width: 846px;
    text-align: center;
    font-family: "EB Garamond", serif;
    letter-spacing: 1px;
  }
  .header-title {
    margin: 0;
    padding-top: 14px;
    font-size: 24px;
    font-weight: 400;
  }
  .header-rule {
    width: 570px;
    height: 1px;
    background: var(--rule);
    margin: 10px auto 0;
  }
  .header-sub {
    margin: 6px 0 0;
    font-size: 14px;
  }
  .item-card {
    position: absolute;
    left: 107px;
    width: 632px;
    height: 189px;
    background: var(--card);
    border: 1px solid var(--card-edge);
    box-shadow: 4px 6px 10px rgba(80, 90, 60, 0.28);
  }
  .item-figure {
    position: absolute;
    left: 16px;
    top: 22px;
    width: 52px;
    height: 120px;
    background: linear-gradient(180deg, var(--figure), var(--figure-light));
    border-radius: 24px 24px 6px 6px;
  }
  .item-figure.is-goods {
    top: 70px;
    width: 64px;
    height: 66px;
    border-radius: 4px 4px 18px 18px;
  }
  .item-category {
    position: absolute;
    left: 14px;
    bottom: 14px;
    font-family: "EB Garamond", serif;
    font-size: 15px;
    color: var(--ink-soft);
  }
  .item-name {
    position: absolute;
    left: 200px;
    width: 270px;
    top: 60px;
    text-align: center;
    font-size: 28px;
    letter-spacing: 2px;
  }
  .item-price {
    position: absolute;
    right: 20px;
    top: 56px;
    font-size: 34px;
    font-weight: 400;
    white-space: nowrap;
  }
  .item-tax {
    position: absolute;
    right: 62px;
    top: 106px;
    font-size: 11px;
    color: var(--ink-soft);
    white-space: nowrap;
  }
  .footer {
    position: absolute;
    left: 0;
    top: 1044px;
    width: 846px;
    height: 156px;
    background: var(--footer);
  }
  .footer-logo-slot {
    position: absolute;
    left: 104px;
    top: 22px;
  }
  .store-label {
    position: absolute;
    left: 578px;
    top: 44px;
    font-size: 22px;
    white-space: nowrap;
  }
</style>
</head>
<body>
  <header class="header">
    <h1 class="header-title">NEW＆RENEWAL</h1>
    <div class="header-rule"></div>
    <p class="header-sub">NEW＆RENEWAL</p>
  </header>

  <section class="item-card" style="top:127px;">
    <div class="item-figure" role="img" aria-label="女性マネキンのシルエット"></div>
    <span class="item-category">ladies</span>
    <div class="item-name">冬物ジャケット</div>
    <div class="item-price">¥1,980</div>
    <div class="item-tax">税込 1,980</div>
  </section>

  <section class="item-card" style="top:355px;">
    <div class="item-figure" role="img" aria-label="男性マネキンのシルエット"></div>
    <span class="item-category">mens</span>
    <div class="item-name">冬物ジャケット</div>
    <div class="item-price">¥1,980</div>
    <div class="item-tax">税込 1,980</div>
  </section>

  <section class="item-card" style="top:587px;">
    <div class="item-figure" role="img" aria-label="男性マネキンのシルエット"></div>
    <span class="item-category">mens</span>
    <div class="item-name">パンツ</div>
    <div class="item-price">¥1,980</div>
    <div class="item-tax">税込 1,980</div>
  </section>

  <section class="item-card" style="top:818px;">
    <div class="item-figure is-goods" role="img" aria-label="雑貨バッグのイラスト"></div>
    <span class="item-category">Items</span>
    <div class="item-name">バッグ</div>
    <div class="item-price">¥1,980</div>
    <div class="item-tax">税込 1,980</div>
  </section>

  <footer class="footer">
    <svg class="footer-logo-slot" width="178" height="92" viewBox="0 0 178 92">
      <rect x="0.5" y="0.5" width="177" height="91" fill="none" stroke="var(--slot-line)" stroke-width="1"/>
      <line x1="0.5" y1="0.5" x2="177.5" y2="91.5" stroke="var(--slot-line)" stroke-width="1"/>
    </svg>
    <div class="store-label">店舗名 |Floor</div>
  </footer>
</body>
</html>
```